Spring Camp flyer

I would like a postcard that promotes our Spring Break Camp, with normal postcard design on reverse side. The target age group for our camp is between 2 and 7 years old, it needs to be very visually appealing and exciting! Vibrant and quite cool so that people want to pick it up and see what it is :)
I love the file titled SpringBrk a lot!
I also need the details
www.bluelantern.ae
info@bluelantern.ae
Camp is 800 aed per week
1200 for both weeks
9am - 2pm with early drop and late pick up available
Um Suqeim 3 location
Daily activities include;
yoga, brain training, language, creative arts, sports and more!
Online gallery updated daily!

```html
<!DOCTYPE html>
<html lang="en">
<head>
<meta charset="utf-8">
<title>Spring Break Camp Postcard</title>
<link href="https://fonts.googleapis.com/css2?family=Rye&family=Smokum&family=Oswald:wght@500&family=Chewy&family=Arimo:wght@400;700&display=swap" rel="stylesheet">
<style>
:root{
  --stage:#2a2a2c;
  --paper:#ffffff;
  --sky-top:#d8ecf7;
  --sky-low:#f4f9fc;
  --grass:#8cc63f;
  --grass-dark:#5e9e2a;
  --teal:#4a8fa8;
  --aqua:#8fd0d8;
  --yellow:#f1c232;
  --red:#d3262b;
  --purple:#7b3f9e;
  --orange:#f58c3f;
  --brown:#7a3a1c;
  --navy:#2b3a78;
  --olive:#a5a832;
  --magenta:#b8338e;
  --pink:#f2a7c8;
  --grey-line:#555;
}
*{margin:0;padding:0;box-sizing:border-box}
html,body{width:1000px;height:1200px;overflow:hidden;background:var(--stage)}
.canvas{position:relative;width:1000px;height:1200px}
.card{position:absolute;overflow:hidden}
.card--front{left:140px;top:27px;width:727px;height:563px}
.card--back{left:144px;top:617px;width:721px;height:558px;background:var(--paper)}

/* front */
.scene{position:absolute;inset:0;background:linear-gradient(180deg,var(--sky-top) 0%,var(--sky-low) 55%,#b9dc7a 78%,var(--grass) 90%,var(--grass-dark) 100%)}
.bunting-band{position:absolute;top:0;height:80px;background:linear-gradient(90deg,#7fc0d2,#e9a6d0,#f59b6b,#f8d66a,#b6d98a);opacity:.45;clip-path:polygon(0 0,100% 0,100% 40%,0 100%)}
.bunting-band--left{left:0;width:300px}
.bunting-band--right{right:0;width:250px;clip-path:polygon(0 0,100% 0,100% 100%,0 40%)}
.trees{position:absolute;left:470px;top:300px;width:257px;height:180px;border-radius:60px 60px 10px 10px;background:radial-gradient(ellipse at 70% 40%,#7cbf3a,#5fa02a 60%,transparent 75%)}
.title{position:absolute;left:0;width:727px;text-align:center;font-family:"Rye",serif;line-height:1;white-space:nowrap}
.title--spring{top:60px;font-size:74px}
.title--break{top:160px;font-size:74px}
.title--camp{top:262px;font-size:96px}
.c-yellow{color:var(--yellow)}.c-aqua{color:var(--aqua)}.c-purple{color:var(--purple)}.c-red{color:var(--red)}
.dates{position:absolute;left:223px;top:452px;width:440px;text-align:center;font-family:"Chewy","Oswald",sans-serif;font-size:25px;line-height:28px;letter-spacing:.5px;white-space:nowrap}
.dates .week{color:var(--purple)}.dates .day{color:var(--red)}
.brand{position:absolute;display:flex;align-items:center;gap:8px;font-family:"Arimo",sans-serif;font-weight:700;color:var(--teal);white-space:nowrap}
.brand__dot{border-radius:50%;background:var(--teal)}
.brand--front{left:52px;top:400px;font-size:24px}
.brand--front .brand__dot{width:26px;height:26px}

/* back */
.bunting-strip{position:absolute;left:0;top:0;width:465px;height:58px;background:linear-gradient(90deg,#f58c3f,#f8d232,#4ab04a,#2f8fd0,#d22d8c,#f58c3f,#4ab04a);opacity:.55;clip-path:polygon(0 30%,50% 0,100% 0,100% 60%,50% 100%,0 75%)}
.badge{position:absolute;border-radius:50%;display:flex;align-items:center;justify-content:center;text-align:center;color:#fff;font-family:"Arimo",sans-serif;line-height:1.2;white-space:nowrap}
.badge--price{left:35px;top:112px;width:96px;height:96px;background:var(--red);border:3px solid var(--teal);font-size:13px}
.badge--hours{left:130px;top:42px;width:124px;height:124px;background:var(--orange);font-size:13px;font-weight:700}
.badge--bundle{left:249px;top:122px;width:88px;height:88px;background:var(--teal);font-size:13px}
.balloon-string{position:absolute;left:0;top:0}
.bird{position:absolute;left:132px;top:206px;width:66px;height:48px;border-radius:50%;background:radial-gradient(circle at 55% 45%,#f7c1d8,var(--pink))}
.activities-head{position:absolute;left:20px;top:272px;width:340px;text-align:center;font-family:"Smokum","Oswald",sans-serif;font-weight:500;font-size:24px;line-height:30px;color:var(--purple);letter-spacing:1px;white-space:nowrap}
.activities-rule{position:absolute;left:52px;top:306px;width:258px;height:1px;background:var(--grey-line)}
.activities{position:absolute;left:10px;top:316px;width:360px;text-align:center;font-family:"Smokum","Oswald",sans-serif;font-weight:500;font-size:22px;line-height:27px;letter-spacing:1px;white-space:nowrap}
.activities span{margin:0 3px}
.a-yoga{color:var(--purple)}.a-brain{color:var(--red)}.a-lang{color:var(--brown)}.a-music{color:var(--magenta)}.a-arts{color:var(--navy)}.a-sports{color:var(--olive)}.a-more{color:var(--teal)}
.contact{position:absolute;left:27px;top:410px;width:321px;height:78px;background:var(--teal);border:2px solid var(--orange);border-radius:30px;color:#fff;font-family:"Arimo",sans-serif;text-align:center;padding-top:7px;white-space:nowrap}
.contact__head{font-size:16px;font-weight:700;letter-spacing:.6px}
.contact__phone{font-size:16px;font-weight:700;margin-top:5px;display:flex;justify-content:center;align-items:center;gap:5px}
.contact__web{font-size:13px;margin-top:4px;display:flex;justify-content:center;gap:12px}
.gallery{position:absolute;left:17px;top:498px;width:341px;text-align:center;font-family:"Chewy","Oswald",sans-serif;font-size:22px;line-height:28px;color:var(--red);letter-spacing:1px;white-space:nowrap}
.brand--back{left:396px;top:96px;font-size:20px}
.brand--back .brand__dot{width:20px;height:20px}
.stamp{position:absolute;left:574px;top:50px;width:94px;height:106px;border:1px solid #999;font-family:"Arimo",sans-serif;font-size:17px;color:#777;padding:24px 0 0 24px;line-height:21px}
.address-line{position:absolute;left:378px;width:296px;height:1px;background:var(--grey-line)}
</style>
</head>
<body>
<main class="canvas">

  <section class="card card--front" aria-label="Postcard front">
    <div class="scene" role="img" aria-label="Illustrated spring meadow with sky, grass, path and trees"></div>
    <div class="bunting-band bunting-band--left" role="img" aria-label="Colourful party bunting"></div>
    <div class="bunting-band bunting-band--right" role="img" aria-label="Colourful party bunting"></div>
    <div class="trees" role="img" aria-label="Illustrated trees"></div>

    <h1 class="title title--spring"><span class="c-yellow">S</span><span class="c-aqua">PRI</span><span class="c-purple">N</span><span class="c-red">G</span></h1>
    <div class="title title--break"><span class="c-aqua">B</span><span class="c-red">R</span><span class="c-aqua">E</span><span class="c-purple">A</span><span class="c-aqua">K</span></div>
    <div class="title title--camp"><span class="c-aqua">C</span><span class="c-red">A</span><span class="c-yellow">M</span><span class="c-aqua">P</span></div>

    <div class="brand brand--front"><span class="brand__dot"></span>Blue Lantern</div>

    <p class="dates">
      <span class="week">WEEK 1</span> <span class="day">- 29 MARCH - 2 APRIL</span><br>
      <span class="week">WEEK 2</span> <span class="day">- 5 APRIL - 9 APRIL</span>
    </p>
  </section>

  <section class="card card--back" aria-label="Postcard back">
    <div class="bunting-strip" role="img" aria-label="Colourful party bunting"></div>

    <svg class="balloon-string" width="360" height="260" aria-hidden="true">
      <path d="M192 166 q8 30 -6 52 q-12 20 -8 40" fill="none" stroke="#9a7a5a" stroke-width="1.2"/>
    </svg>
    <div class="badge badge--hours"><span>9 - 2pm<br>with early drop<br>and late pick up<br>available</span></div>
    <div class="badge badge--price"><span><b>800</b> <i>AED</i><br>PER WEEK</span></div>
    <div class="badge badge--bundle"><span>1200<br>aed for<br>2 weeks</span></div>
    <div class="bird" role="img" aria-label="Small pink bird illustration"></div>

    <h2 class="activities-head">DAILY ACTIVITIES INCLUDE</h2>
    <div class="activities-rule"></div>
    <p class="activities">
      <span class="a-yoga">YOGA</span><span class="a-brain">BRAIN TRAINING</span><span class="a-lang">LANGUAGE</span><br>
      <span class="a-music">MUSIC</span><span class="a-arts">CREATIVE ARTS</span><span class="a-sports">SPORTS</span><br>
      <span class="a-more">AND MORE!</span>
    </p>

    <div class="contact">
      <div class="contact__head">Contact for More Information</div>
      <div class="contact__phone">
        <svg width="14" height="14" viewBox="0 0 24 24" aria-hidden="true"><circle cx="12" cy="12" r="11" fill="none" stroke="#fff" stroke-width="1.5"/><path d="M8 6c-1 1-1 3 1 6s4 5 6 5l1-2-2-1-1 1c-1 0-3-2-3-3l1-1-1-2z" fill="#fff"/></svg>
        +971 4 555 0142
      </div>
      <div class="contact__web"><span>www.bluelantern.ae</span><span>info@bluelantern.ae</span></div>
    </div>
    <p class="gallery">GALLERY UPDATED DAILY</p>

    <div class="brand brand--back"><span class="brand__dot"></span>Blue Lantern</div>
    <div class="stamp">Place<br>Stamp<br>Here</div>
    <div class="address-line" style="top:262px"></div>
    <div class="address-line" style="top:322px"></div>
    <div class="address-line" style="top:382px"></div>
  </section>

</main>
</body>
</html>
```